BRIGHTDESK COWORKING Website design and coding

BRIGHTDESK COWORKING

BRIGHTDESK is Galveston’s first (and currently only) shared business co-working space. We share the same upscale, casual work environment, but we work independently on our own (or our team’s) projects and goals. For only a flat $195 membership fee per month, you have your very own all-inclusive, fun, personal business office environment. Website is written (Word file #12, below); and all pictures etc provided. Galveston is a beachy, coastal, historic city an hour from Houston, Texas USA. Logo (file 11 below) is temporary only.

Target Market(s)

Outside sales people, medical students looking for study hall, Houston companies looking for local office, real estate agents, graphic artists, entrepreneurs, etc

Contact Information for Business Card

will discuss --want to combine with current business card with multiple businesses

Logo Text

BRIGHTDESK COWORKING

Coding

Coded - Design and coding required

Number of Pages Required

5+ page

Colors
ec1f27
fbed22

Requirements
Nice to have
• maroon/wine dominant with yellow and red accents, gray base are the colors of the space--website could coordinate--but open to creative ideas/combinations

```html
<!DOCTYPE html>
<html lang="en">
<head>
<meta charset="utf-8">
<title>Brightdesk Coworking – Website Design</title>
<link href="https://fonts.googleapis.com/css2?family=Poppins:wght@400;500;600;700&display=swap" rel="stylesheet">
<style>
:root{
  --red:#ec1f27;
  --pink:#f76f82;
  --blush:#ffd9de;
  --ink:#1f1f1f;
  --grey:#8a8a8a;
  --line:#c9c9c9;
  --paper:#ffffff;
  --mist:#f1f1f3;
  --night:#2b2c2f;
}
*{margin:0;padding:0;box-sizing:border-box}
html,body{width:1200px;height:675px;overflow:hidden;background:var(--paper)}
body{position:relative;font-family:'Poppins',sans-serif;color:var(--ink)}
.deco-circle{position:absolute;width:332px;height:332px;border-radius:50%;background:var(--pink);top:171px}
.deco-circle.left{left:-199px}
.deco-circle.right{left:1077px}

.page{position:absolute;background:var(--paper);overflow:hidden;box-shadow:0 2px 10px rgba(0,0,0,.12)}
.abs{position:absolute}
.tiny{font-size:3px;line-height:4.4px;color:var(--grey)}
.heading{font-size:5.5px;font-weight:700;color:var(--red);text-transform:uppercase;letter-spacing:.2px;text-align:center}
.btn{position:absolute;background:var(--red);color:#fff;font-size:2.8px;font-weight:600;text-align:center;border-radius:1.5px;text-transform:uppercase;white-space:nowrap}
.btn.ghost{background:#fff;color:var(--red);border:.8px solid var(--red)}
.photo{position:absolute}

/* membership page */
.membership{left:172px;top:80px;width:290px;height:489px}
.membership-hero{left:0;top:0;width:290px;height:57px;background:linear-gradient(90deg,#c9ccd2,#e7e8ec 40%,#b9bcc2 70%,#d9dade)}
.membership-hero .veil{position:absolute;inset:0;background:rgba(255,255,255,.55)}
.plan{position:absolute;top:70px;width:76px;height:170px;background:#fff;border-radius:4px;box-shadow:0 0 4px rgba(0,0,0,.1);text-align:center}
.plan.featured{background:var(--blush)}
.plan-icon{width:32px;height:32px;margin:9px auto 0;border-radius:50%;border:1px solid var(--red);display:flex;align-items:center;justify-content:center;background:#fff}
.plan.featured .plan-icon{background:var(--red)}
.plan-name{font-size:3.4px;margin-top:3px}
.plan-price{font-size:6px;font-weight:500;margin-top:3px}
.plan-price small{font-size:4px}
.plan-list{list-style:none;text-align:left;margin:5px 0 0 8px}
.plan-list li{font-size:3px;line-height:10.8px;color:#555;display:flex;gap:3px;align-items:center}
.plan-list li.off{color:#bbb}
.mark{color:var(--red);font-weight:700;font-size:3.6px}
.off .mark{color:#777}

/* home page */
.home{left:462px;top:33px;width:275px;height:551px}
.topbar{left:0;top:0;width:275px;height:6px;background:var(--red)}
.nav{left:0;top:6px;width:275px;height:17px;display:flex;align-items:center;padding:0 22px}
.brand{display:flex;align-items:center;gap:2px;font-size:4.4px;font-weight:500}
.brand i{width:5px;height:5px;background:var(--red);display:block}
.nav-links{display:flex;gap:10px;margin-left:30px;font-size:2.4px;color:#555}
.hero{left:0;top:23px;width:275px;height:131px;background:linear-gradient(160deg,#4a4237,#8a6a3d 45%,#2e2a25)}
.hero-text{position:absolute;left:0;right:0;top:44px;text-align:center;color:#fff}
.hero-text .kicker{font-size:2.8px;letter-spacing:.3px}
.hero-text h1{font-size:9.4px;font-weight:700;line-height:14px;margin-top:2px}
.hero-arrow{position:absolute;top:64px;width:7px;height:7px;border-radius:50%;background:#fff}
.about-title{font-size:5px;font-weight:600;color:var(--red)}
.amenities{left:0;top:341px;width:275px;height:210px;background:linear-gradient(#ededee,#f7f7f7)}
.amenity{position:absolute;width:71px;height:68px;background:#fff;box-shadow:0 0 3px rgba(0,0,0,.1);text-align:center}
.amenity.featured{background:var(--blush)}
.amenity-icon{width:14px;height:14px;margin:7px auto 2px;border-radius:50%;display:flex;align-items:center;justify-content:center}
.amenity.featured .amenity-icon{background:var(--red)}
.amenity h3{font-size:3.6px;font-weight:500}
.amenity p{font-size:2.4px;line-height:3.6px;color:var(--grey);margin:3px 6px 0}
.amenity .more{font-size:2.4px;color:var(--red);margin-top:2px}

/* philosophy + contact page */
.contact{left:737px;top:67px;width:300px;height:485px}
.philosophy{left:0;top:0;width:300px;height:234px;background:linear-gradient(#efeff1,#e1e2e5)}
.value{position:absolute;width:130px;text-align:center}
.value-icon{width:32px;height:32px;margin:0 auto;border-radius:50%;border:1px solid var(--red);background:#fff;display:flex;align-items:center;justify-content:center}
.value h3{font-size:4.6px;font-weight:700;color:var(--red);margin-top:4px;text-transform:uppercase}
.value p{font-size:2.6px;line-height:4px;color:var(--grey);margin:2px 14px 0}
.value .more{font-size:2.4px;color:var(--red)}
.map{left:0;top:234px;width:125px;height:226px;background:linear-gradient(150deg,#3a3b3f,#262729 60%,#1d1e20)}
.field{position:absolute;left:148px;width:117px;border:.9px solid var(--pink);border-radius:2px;background:#fff;font-size:2.6px;color:#aaa;padding:3px}
.footer{left:0;top:460px;width:300px;height:25px;background:#0d0d0d;display:flex;align-items:center;padding:0 8px;color:#ccc;font-size:2.6px}
.footer-links{display:flex;gap:10px;margin-left:auto;margin-right:10px}
.dot{width:5px;height:5px;border-radius:50%;background:#eee;display:inline-block;margin-left:2px}

.signature{position:absolute;left:0;width:1200px;top:610px;display:flex;justify-content:center;align-items:center;gap:6px}
.signature i{width:16px;height:16px;background:var(--red);display:block}
.signature span{font-size:24px;font-weight:400;color:var(--ink)}
</style>
</head>
<body>
<div class="deco-circle left"></div>
<div class="deco-circle right"></div>

<!-- Membership page -->
<section class="page membership">
  <div class="abs membership-hero" role="img" aria-label="Faded photo of the coworking space interior"><div class="veil"></div></div>
  <div class="abs heading" style="left:0;right:0;top:20px">Our Membership</div>
  <div class="abs tiny" style="left:80px;right:80px;top:29px;text-align:center">Brightdesk is the first shared business co-working space in town, offering all of the following benefits to every monthly member</div>

  <div class="plan featured" style="left:26px">
    <div class="plan-icon"><svg width="16" height="12" viewBox="0 0 16 12"><rect x="1" y="1" width="14" height="3" fill="none" stroke="#fff" stroke-width="1"/><path d="M3 4v7M13 4v7M5 7h6" stroke="#fff" stroke-width="1"/></svg></div>
    <div class="plan-name">Co-working</div>
    <div class="plan-price">$195<small>/mo</small></div>
    <ul class="plan-list">
      <li><span class="mark">✓</span>24/7</li><li><span class="mark">✓</span>Free wifi</li><li><span class="mark">✓</span>Use of the kitchen</li><li><span class="mark">✓</span>Cleaning service</li><li><span class="mark">✓</span>conference room</li><li><span class="mark">✓</span>Use of the Office</li><li><span class="mark">✓</span>Utilities included</li>
    </ul>
    <div class="btn" style="left:20px;top:151px;width:36px;height:9px;line-height:9px">Book now</div>
  </div>
  <div class="plan" style="left:113px">
    <div class="plan-icon"><svg width="16" height="14" viewBox="0 0 16 14"><circle cx="6" cy="4" r="2.5" fill="none" stroke="#333" stroke-width="1"/><path d="M2 13v-3a4 4 0 0 1 8 0v3M9 9h6v4" fill="none" stroke="#333" stroke-width="1"/></svg></div>
    <div class="plan-name">Virtual Office</div>
    <div class="plan-price">$145<small>/mo</small></div>
    <ul class="plan-list">
      <li><span class="mark">✓</span>24/7</li><li><span class="mark">✓</span>Free wifi</li><li><span class="mark">✓</span>Use of the kitchen</li><li><span class="mark">✓</span>Cleaning service</li><li><span class="mark">✓</span>conference room</li><li><span class="mark">✓</span>Use of the Office</li><li class="off"><span class="mark">✕</span>Utilities included</li>
    </ul>
    <div class="btn ghost" style="left:20px;top:151px;width:36px;height:9px;line-height:8px">Book now</div>
  </div>
  <div class="plan" style="left:197px">
    <div class="plan-icon"><svg width="16" height="12" viewBox="0 0 16 12"><rect x="1" y="1" width="14" height="3" fill="none" stroke="#333" stroke-width="1"/><path d="M3 4v7M13 4v7M9 4v4h4" stroke="#333" stroke-width="1" fill="none"/></svg></div>
    <div class="plan-name">Virtual Office</div>
    <div class="plan-price">$120<small>/mo</small></div>
    <ul class="plan-list">
      <li><span class="mark">✓</span>24/7</li><li><span class="mark">✓</span>Free wifi</li><li><span class="mark">✓</span>Use of the kitchen</li><li><span class="mark">✓</span>Cleaning service</li><li><span class="mark">✓</span>conference room</li><li class="off"><span class="mark">✕</span>Use of the Office</li><li class="off"><span class="mark">✕</span>Utilities included</li>
    </ul>
    <div class="btn ghost" style="left:20px;top:151px;width:36px;height:9px;line-height:8px">Book now</div>
  </div>

  <div class="abs" style="left:0;right:0;top:286px;text-align:center;font-size:5px;font-weight:600;color:var(--red)">Gallery</div>
  <div class="abs" style="left:0;right:0;top:296px;text-align:center;font-size:3px">Check Our Photo</div>
  <div class="photo" style="left:26px;top:310px;width:250px;height:75px;background:linear-gradient(100deg,#7a3a2c,#c79a6a 40%,#3b3632 75%,#6b6359)" role="img" aria-label="Photo of the open lounge and work tables"></div>
  <div class="photo" style="left:26px;top:385px;width:125px;height:73px;background:linear-gradient(120deg,#9c2b34,#5b5552 55%,#b8b08c)" role="img" aria-label="Photo of lockers and a plant in the hallway"></div>
  <div class="photo" style="left:151px;top:385px;width:125px;height:73px;background:linear-gradient(120deg,#3a3532,#7b6a5a 50%,#d8c9b8)" role="img" aria-label="Photo of the shared kitchen"></div>
</section>

<!-- Home page -->
<section class="page home">
  <div class="abs topbar"></div>
  <div class="abs tiny" style="left:22px;top:0;color:#fff;font-size:2.4px;line-height:6px">(555) 014-2290 &nbsp;&nbsp; hello@brightdesk.co</div>
  <nav class="abs nav">
    <div class="brand"><i></i>Brightdesk</div>
    <div class="nav-links"><span style="color:var(--red)">Home</span><span>About us</span><span>Pictures</span><span>Amenities</span><span>Membership</span><span>Contact us</span></div>
    <div class="btn" style="left:217px;top:4px;width:36px;height:8px;line-height:8px">Schedule a tour</div>
  </nav>
  <div class="abs hero" role="img" aria-label="Photo of the workspace with pendant lamps and large windows">
    <div class="hero-text">
      <div class="kicker">THE BEST WORKSPACE IN TOWN</div>
      <h1>Professionals, Creative,<br>Flexible, Scalable Workspace</h1>
    </div>
    <div class="btn" style="left:116px;top:87px;width:43px;height:9px;line-height:9px">Book a tour</div>
    <div class="hero-arrow" style="left:10px"></div>
    <div class="hero-arrow" style="left:258px;background:var(--red)"></div>
  </div>

  <div class="photo" style="left:33px;top:182px;width:96px;height:60px;background:linear-gradient(130deg,#d7c79a,#8b7a5d 60%,#c7b08a);border:1px solid #333" role="img" aria-label="Photo of lamps over a desk"></div>
  <div class="photo" style="left:0;top:200px;width:92px;height:48px;background:linear-gradient(130deg,#6b6761,#b8b2a6 50%,#3a3837);border:1px solid #fff" role="img" aria-label="Photo of a meeting room"></div>
  <div class="photo" style="left:0;top:258px;width:110px;height:60px;background:linear-gradient(120deg,#2f2b29,#8c6f4f 45%,#d8b63a 80%);border:1px solid #fff" role="img" aria-label="Photo of lounge seating with yellow chairs"></div>
  <div class="photo" style="left:110px;top:280px;width:19px;height:39px;background:#3a2e2c"></div>

  <div class="abs about-title" style="left:137px;top:210px">About us</div>
  <div class="abs tiny" style="left:137px;top:220px;width:110px">Brightdesk is the first shared business co-working space in the area. We share the same upscale space</div>
  <div class="abs tiny" style="left:137px;top:234px;width:52px"><b style="color:#333">Trusted by Thousands</b><br>Members grow their work here every single day</div>
  <div class="abs tiny" style="left:195px;top:234px;width:52px"><b style="color:#333">Workspace Solutions</b><br>Flexible desks and offices for every team</div>
  <div class="abs tiny" style="left:137px;top:263px;width:110px">Work independently on your own projects and goals in a bright shared office.</div>
  <div class="btn" style="left:137px;top:284px;width:31px;height:9px;line-height:9px">Read more</div>

  <div class="abs amenities">
    <div class="heading" style="position:absolute;left:0;right:0;top:21px">Our Amenities</div>
    <div class="tiny" style="position:absolute;left:70px;right:70px;top:30px;text-align:center">Every membership includes all of the following amenities for a flat monthly fee</div>
  </div>
  <div class="amenity featured" style="left:22px;top:384px"><div class="amenity-icon"><svg width="8" height="8" viewBox="0 0 8 8"><circle cx="4" cy="4" r="3" fill="none" stroke="#fff" stroke-width=".8"/><path d="M4 2v2h1.5" stroke="#fff" stroke-width=".8" fill="none"/></svg></div><h3>Daily open</h3><p>Come in any day of the week and settle into your own desk</p><div class="more">Learn More</div></div>
  <div class="amenity" style="left:101px;top:384px"><div class="amenity-icon"><svg width="8" height="8" viewBox="0 0 8 8"><path d="M1 4a4 4 0 0 1 6 0M2.3 5.3a2 2 0 0 1 3.4 0" stroke="#ec1f27" stroke-width=".8" fill="none"/><circle cx="4" cy="6.6" r=".7" fill="#ec1f27"/></svg></div><h3>Free wifi</h3><p>Fast and secure internet for every member at every desk</p><div class="more">Learn More</div></div>
  <div class="amenity" style="left:180px;top:384px"><div class="amenity-icon"><svg width="8" height="8" viewBox="0 0 8 8"><circle cx="4" cy="4" r="3" fill="none" stroke="#ec1f27" stroke-width=".8"/><path d="M4 2v2h1.5" stroke="#ec1f27" stroke-width=".8" fill="none"/></svg></div><h3>24 Hour</h3><p>Access the space day or night whenever your work calls</p><div class="more">Learn More</div></div>
  <div class="amenity" style="left:22px;top:460px"><div class="amenity-icon"><svg width="8" height="8" viewBox="0 0 8 8"><path d="M4 7.5S1.5 4.8 1.5 3a2.5 2.5 0 0 1 5 0C6.5 4.8 4 7.5 4 7.5z" stroke="#ec1f27" stroke-width=".8" fill="none"/></svg></div><h3>Great location</h3><p>Steps from the historic downtown and a short drive to the beach</p><div class="more">Learn More</div></div>
  <div class="amenity" style="left:101px;top:460px"><div class="amenity-icon"><svg width="8" height="8" viewBox="0 0 8 8"><rect x="2" y="1" width="4" height="6" fill="none" stroke="#ec1f27" stroke-width=".8"/></svg></div><h3>Private Lockable</h3><p>Keep your things safe in your own private lockable storage</p><div class="more">Learn More</div></div>
  <div class="amenity" style="left:180px;top:460px"><div class="amenity-icon"><svg width="8" height="8" viewBox="0 0 8 8"><circle cx="4" cy="2.5" r="1.5" fill="none" stroke="#ec1f27" stroke-width=".8"/><path d="M1.5 7.5a2.5 2.5 0 0 1 5 0" stroke="#ec1f27" stroke-width=".8" fill="none"/></svg></div><h3>Conference Rooms</h3><p>Meet clients and teams in a quiet fully equipped room</p><div class="more">Learn More</div></div>
  <div class="abs" style="left:135px;top:533px;width:4px;height:4px;border-radius:50%;background:var(--red)"></div>
</section>

<!-- Philosophy and contact page -->
<section class="page contact">
  <div class="abs philosophy">
    <div class="heading" style="position:absolute;left:0;right:0;top:22px">The Brightdesk Philosophy</div>
    <div class="tiny" style="position:absolute;left:75px;right:75px;top:31px;text-align:center">Brightdesk is the first shared business co-working space, offering the following to every member</div>
  </div>
  <div class="value" style="left:7px;top:54px"><div class="value-icon"><svg width="14" height="14" viewBox="0 0 14 14"><path d="M2 13V6l5-4 5 4v7zM5 13V9h4v4" fill="none" stroke="#ec1f27" stroke-width=".9"/></svg></div><h3>Work outside the home</h3><p>Lorem ipsum dolor sit amet, consectetur adipiscing elit, sed do eiusmod tempor</p><div class="more">Read more +</div></div>
  <div class="value" style="left:141px;top:54px"><div class="value-icon"><svg width="14" height="14" viewBox="0 0 14 14"><circle cx="7" cy="6" r="4" fill="none" stroke="#ec1f27" stroke-width=".9"/><path d="M5 10l-1 3 3-1 3 1-1-3" fill="none" stroke="#ec1f27" stroke-width=".9"/></svg></div><h3>Brightdesk the competition</h3><p>Lorem ipsum dolor sit amet, consectetur adipiscing elit, sed do eiusmod tempor</p><div class="more">Read more +</div></div>
  <div class="value" style="left:7px;top:139px"><div class="value-icon"><svg width="14" height="14" viewBox="0 0 14 14"><circle cx="4" cy="5" r="1.6" fill="none" stroke="#ec1f27" stroke-width=".9"/><circle cx="10" cy="5" r="1.6" fill="none" stroke="#ec1f27" stroke-width=".9"/><path d="M1 11a3 3 0 0 1 6 0M7 11a3 3 0 0 1 6 0" fill="none" stroke="#ec1f27" stroke-width=".9"/></svg></div><h3>Work with your coworkers</h3><p>Lorem ipsum dolor sit amet, consectetur adipiscing elit, sed do eiusmod tempor</p><div class="more">Read more +</div></div>
  <div class="value" style="left:141px;top:139px"><div class="value-icon"><svg width="14" height="14" viewBox="0 0 14 14"><path d="M2 12l4-7 3 4 3-5M6 2v3" fill="none" stroke="#ec1f27" stroke-width=".9"/></svg></div><h3>Path to your success</h3><p>Lorem ipsum dolor sit amet, consectetur adipiscing elit, sed do eiusmod tempor</p><div class="more">Read more +</div></div>

  <div class="abs map" role="img" aria-label="Dark map with a pin marking the coworking location"></div>

  <div class="abs" style="left:148px;top:266px;font-size:5.2px;font-weight:600;color:var(--red)">Contact us</div>
  <svg class="abs" style="left:148px;top:283px" width="4" height="5" viewBox="0 0 8 10"><path d="M4 10S0 6 0 4a4 4 0 0 1 8 0c0 2-4 6-4 6z" fill="#ec1f27"/></svg>
  <div class="abs tiny" style="left:155px;top:282px;width:60px;font-size:2.6px;line-height:3.8px;color:#555">Brightdesk Coworking<br>410 Harbor Row<br>Port Merrow, ST 00412</div>
  <svg class="abs" style="left:218px;top:283px" width="5" height="5" viewBox="0 0 10 10"><path d="M2 0l2 3-1 1.5a6 6 0 0 0 2.5 2.5L7 6l3 2-1 2C4 10 0 6 0 1z" fill="#ec1f27"/></svg>
  <div class="abs tiny" style="left:226px;top:282px;font-size:2.6px;color:#555">(555) 014-2290</div>
  <svg class="abs" style="left:218px;top:296px" width="5" height="4" viewBox="0 0 10 8"><rect width="10" height="8" fill="#ec1f27"/></svg>
  <div class="abs tiny" style="left:226px;top:295px;font-size:2.6px;color:#555">hello@brightdesk.co</div>

  <div class="field" style="top:319px;height:15px">Name</div>
  <div class="field" style="top:344px;height:17px">Email</div>
  <div class="field" style="top:370px;height:36px">Message</div>
  <div class="btn" style="left:148px;top:416px;width:37px;height:12px;line-height:12px">Send</div>

  <footer class="abs footer">
    <span>© 2024 Brightdesk Coworking. All rights reserved</span>
    <div class="footer-links"><span>Home</span><span>About us</span><span>Pictures</span><span>Contact us</span></div>
    <span class="dot"></span><span class="dot"></span><span class="dot"></span>
  </footer>
</section>

<div class="signature"><i></i><span>Brightdesk Coworking</span></div>
</body>
</html>
```